Webpage layout and company logo combination

We are trying to renovate an existing site to make it sharper and sophisticated in appearance. This is the existing site: http://www.pellmoorrealtynj.com/agents.html . The new presentation should be bright, sharp, sophisticated and should incorporate two additional menu tabs. The menu tabs will be revised as follows: Property Listings, Property Management, Advisory & Consulting, Local Info, R/E Tools, Our Team (please disregard Korean language characters, which will be installed after English version is completed, separately).

It Company

```html
<!DOCTYPE html>
<html lang="en">
<head>
<meta charset="utf-8">
<title>Pellmoor Realty</title>
<link href="https://fonts.googleapis.com/css2?family=Open+Sans:wght@400;600&family=Lato:wght@400;700&display=swap" rel="stylesheet">
<style>
:root{
  --topbar:#c6cf98;
  --plum:#6b2a45;
  --nav-a:#b0457d;
  --nav-b:#8e2f60;
  --ink:#222;
  --muted:#888;
  --card-bg:#f2f2f2;
  --card-line:#b9c48c;
  --footer:#2b2b2b;
  --footer-base:#232323;
  --footer-text:#ddd;
  --magenta:#b0386f;
}
*{margin:0;padding:0;box-sizing:border-box}
html,body{width:700px;height:1200px;overflow:hidden}
body{position:relative;font-family:"Open Sans",Arial,sans-serif;color:var(--ink);background:#fff}
.abs{position:absolute}
.topbar{left:0;top:0;width:700px;height:35px;background:var(--topbar)}
.brand{left:64px;top:5px;display:flex;align-items:center;gap:7px;font-size:19px;font-weight:600;color:var(--plum);letter-spacing:.3px}
.brand-mark{width:20px;height:20px;border-radius:50%;background:var(--plum)}
.nav{left:0;top:35px;width:700px;height:27px;background:linear-gradient(var(--nav-a),var(--nav-b));display:flex;align-items:center;padding-left:64px;color:#fff;font-size:9.5px}
.nav a{color:#fff;text-decoration:none;margin-right:31px}
.nav svg{margin-right:22px}
.hero{left:0;top:62px;width:700px;height:255px;background:linear-gradient(100deg,#d8cfc4 0%,#efe9e1 40%,#e3d8cc 70%,#c9b49c 100%)}
.hero-panel{left:64px;top:152px;width:303px;height:119px;background:rgba(90,90,90,.78);color:#fff;padding:9px 18px}
.hero-panel h1{font-weight:400;font-size:30px;line-height:1.2;margin-bottom:8px}
.hero-panel p{font-size:8.6px;line-height:1.6;text-align:justify}
.arrow{top:170px;width:31px;height:36px;background:#111;display:flex;align-items:center;justify-content:center}
.services{left:0;top:317px;width:700px;height:145px;background:linear-gradient(#ececec,#fafafa)}
.service{width:200px;text-align:center;top:339px;color:var(--plum);font-size:11.5px;font-weight:600;line-height:1.2}
.service .ring{width:86px;height:86px;margin:0 auto 9px;border-radius:50%;background:var(--plum);border:3px solid #fff;box-shadow:0 0 0 1px #ddd;display:flex;align-items:center;justify-content:center}
h2{font-weight:400;font-size:12px}
.card{top:518px;width:134px;height:166px;background:var(--card-bg);border:1px solid #ddd;border-bottom:3px solid var(--card-line)}
.card .photo{height:92px;background:linear-gradient(#6fa1d8 0%,#b7cfe6 45%,#b8a58c 65%,#7f9a5f 100%)}
.card .tag{position:absolute;right:0;top:79px;background:var(--card-line);color:#fff;font-size:7.5px;padding:1px 5px}
.card .addr{padding:9px 10px 0;font-size:7.5px;line-height:1.8}
.card .addr span{color:var(--muted)}
.card .price{margin:6px 6px 0;border-top:1px solid #ccc;padding:7px 4px;font-size:7.5px}
.agent{width:220px;text-align:center;top:760px}
.agent .face{width:100px;height:100px;margin:0 auto;border-radius:50%;border:3px solid #fff;box-shadow:0 0 0 1px #ddd}
.agent .name{margin-top:24px;font-size:10.5px;letter-spacing:.6px}
.agent .role{margin-top:8px;font-size:8.5px;letter-spacing:.4px}
.agent .contact{margin-top:9px;font-size:7.4px;line-height:1.75;letter-spacing:.3px}
.footer{left:0;top:970px;width:700px;height:172px;background:var(--footer);font-family:"Lato",Arial,sans-serif;color:var(--footer-text)}
.footer h3{font-weight:400;font-size:9px;color:#fff;margin-bottom:13px}
.fcol{position:absolute;top:30px}
.fcol p{font-size:7px;line-height:1.6}
.news{display:flex;gap:8px;margin-bottom:25px}
.news .thumb{width:42px;height:36px;flex:none;border:2px solid #555;background:linear-gradient(#6e90b8,#c8d6e5)}
.news p{font-size:7.8px;line-height:1.9}
.news small{font-size:6.6px}
.mail{width:120px;height:24px;border:1px solid #666;color:#888;font-size:8px;padding:5px 9px}
.subscribe{margin-top:13px;width:72px;height:24px;background:var(--magenta);color:#fff;font-size:8px;display:flex;align-items:center;justify-content:center}
.base{left:0;top:1142px;width:700px;height:58px;background:var(--footer-base);border-top:1px solid #3a3a3a;font-family:"Lato",Arial,sans-serif;font-size:6.2px;color:#888;text-align:center;padding-top:16px}
</style>
</head>
<body>
<div class="abs topbar"></div>
<div class="abs brand"><span class="brand-mark"></span>Pellmoor Realty</div>

<nav class="abs nav">
  <svg width="18" height="14" viewBox="0 0 18 14"><path d="M9 0 0 7h2.5v7h4.5V9.5h4V14h4.5V7H18z" fill="#fff"/></svg>
  <a>Property Listings</a><a>Property Management</a><a>Advisory &amp; Consulting</a><a>Local Info</a><a>R/E Tools</a><a>Our Team</a>
</nav>

<div class="abs hero" role="img" aria-label="Couple with an agent viewing a bright empty room"></div>
<div class="abs hero-panel">
  <h1>Pellmoor Realty</h1>
  <p>Pellmoor Realty is your online resource of buying, selling and financing for your residential or commercial real estate.We will assist your real estate needs with our integrity and helpful experience.</p>
</div>
<div class="abs arrow" style="left:0"><svg width="10" height="16"><path d="M8 1 2 8l6 7" stroke="#fff" stroke-width="1.6" fill="none"/></svg></div>
<div class="abs arrow" style="left:669px"><svg width="10" height="16"><path d="M2 1l6 7-6 7" stroke="#fff" stroke-width="1.6" fill="none"/></svg></div>

<div class="abs services"></div>
<div class="abs service" style="left:57px">
  <div class="ring"><svg width="44" height="40" viewBox="0 0 44 40"><path d="M22 2 2 20h5v18h12V26h6v12h12V20h5z" fill="#fff"/></svg></div>
  Property Management &amp;<br>Consulting
</div>
<div class="abs service" style="left:249px">
  <div class="ring"><svg width="44" height="40" viewBox="0 0 44 40"><path d="M4 4h36l3 10H1z" fill="#fff"/><rect x="6" y="17" width="32" height="20" fill="#fff"/><rect x="12" y="22" width="20" height="12" fill="#6b2a45"/></svg></div>
  Commercial
</div>
<div class="abs service" style="left:445px">
  <div class="ring"><svg width="40" height="46" viewBox="0 0 40 46"><circle cx="22" cy="6" r="4" fill="none" stroke="#fff" stroke-width="2.5"/><path d="M22 10v12" stroke="#fff" stroke-width="2.5"/><path d="M18 22 4 36l8 8 14-14z" fill="#fff"/></svg></div>
  Residential
</div>

<h2 class="abs" style="left:64px;top:480px">Latest Property</h2>
<div class="abs card" style="left:64px"><div class="photo" role="img" aria-label="Two-storey suburban house"></div><span class="tag">RENT</span><div class="addr">28 Brookline Lane<br><span>Fairmont East, NJ 0712</span></div><div class="price">$.650.00 / Month</div></div>
<div class="abs card" style="left:210px"><div class="photo" role="img" aria-label="Brick house with triple garage"></div><span class="tag">SALE</span><div class="addr">28 Brookline Lane<br><span>Fairmont East, NJ 0712</span></div><div class="price">$.9050.00</div></div>
<div class="abs card" style="left:356px"><div class="photo" role="img" aria-label="White villa with red roof"></div><span class="tag">RENT</span><div class="addr">28 Brookline Lane<br><span>Fairmont East, NJ 0712</span></div><div class="price">$.650.00 / Month</div></div>
<div class="abs card" style="left:502px"><div class="photo" role="img" aria-label="White villa with red roof"></div><span class="tag">RENT</span><div class="addr">28 Brookline Lane<br><span>Fairmont East, NJ 0712</span></div><div class="price">$.650.00 / Month</div></div>

<h2 class="abs" style="left:64px;top:721px">Our Agents</h2>
<div class="abs agent" style="left:47px"><div class="face" role="img" aria-label="Agent portrait" style="background:linear-gradient(#8a6a44,#3a2a1e)"></div><div class="name">HARLAN PELLMOOR</div><div class="role">Broker/Owner</div><div class="contact">Direct: 555-310-4420 Office: 555-310-4421<br>Cell: 555-310-4477 hpell@mailbox.test</div></div>
<div class="abs agent" style="left:239px"><div class="face" role="img" aria-label="Agent portrait" style="background:linear-gradient(#6f8a5a,#b9c7d8)"></div><div class="name">Nadia Wren</div><div class="role">Sales Agent</div><div class="contact">Direct: 555-310-4420 Office: 555-310-4421<br>Cell: 555-310-4477 hpell@mailbox.test</div></div>
<div class="abs agent" style="left:435px"><div class="face" role="img" aria-label="Agent portrait" style="background:linear-gradient(#d8c9a8,#b08a68)"></div><div class="name">Tobias Kerrick</div><div class="role">Sales Agent</div><div class="contact">Direct: 555-310-4420 Office: 555-310-4421<br>Cell: 555-310-4477 hpell@mailbox.test</div></div>

<footer class="abs footer">
  <div class="fcol" style="left:61px;width:150px">
    <h3>CONTACT INFO</h3>
    <p>Lorem ipsum dolor sit amet, consectetur adipisicing elit, sed do eiusmod tempor</p>
    <p style="margin-top:12px">(123) 1234 456789</p>
    <p style="margin-top:8px">info@youmailinfo.com</p>
  </div>
  <div class="fcol" style="left:256px;width:200px">
    <h3>LATEST NEWS</h3>
    <div class="news"><div class="thumb" role="img" aria-label="City tower"></div><p>Lorem ipsum dolor sit amet, consectetur adipisicing elit, sed do eiusmod tempor<br><small>july 7, 2014</small></p></div>
    <div class="news"><div class="thumb" role="img" aria-label="Glass office building"></div><p>Lorem ipsum dolor sit amet, consectetur adipisicing elit, sed do eiusmod tempor<br><small>july 7, 2014</small></p></div>
  </div>
  <div class="fcol" style="left:510px;width:150px">
    <h3>SUBSCRIBE TO OUR NEWSLETTER</h3>
    <div class="mail">Enter Your Mail Id</div>
    <div class="subscribe" style="margin-left:1px">Subscribe</div>
  </div>
</footer>
<div class="abs base">© Copyright 2014 &nbsp;pellmoor.test . All Rights Reserved</div>
</body>
</html>
```